Shipping Container Sales & Leasing Flyer

We need a flyer that is going to be presented and left behind while prospecting potential customers. The service we are selling is the sale, rental and customization of 20' and 40' shipping containers.

We provide new and used containers to customers for various reasons, mainly storage. We also custom modify containers into storage units, mobile offices, mobile job site storage, command centers, pump houses, garages, living space, the only limit is the customers imagination.

I would like our company logo and phone / email at the bottom but the design should showcase some of the attached images ive provided as examples and have spots where we can list the types of equipment we have for sale and the various types of conversions we can offer.

Please also tie in to the colour scheme of our logo.

Target Market(s)

Moving & Storage, Construction, Contractors, Business to Business, Any business that needs portable storage, Landscapers, Property Maintenance companies.

Industry/Entity Type

Shipping

Font styles to use
Serif
Sans Serif

Requirements
Must have
• Professional feel, clean original design.
Nice to have
• Tie in to our logo colour scheme.
Should not have
• Bulky or crowded look

```html
<!DOCTYPE html>
<html lang="en">
<head>
<meta charset="utf-8">
<title>Containers — Sale, Rental &amp; Customization</title>
<link href="https://fonts.googleapis.com/css2?family=Montserrat:wght@700;800&family=Noto+Sans:wght@400;700&display=swap" rel="stylesheet">
<style>
  :root {
    --green: #6ba140;
    --green-dark: #3f7d35;
    --panel-grey: #737373;
    --band-grey: #e7e7e7;
    --white: #ffffff;
    --photo-blue: #5d7fae;
    --photo-light: #d9dde3;
    --photo-sand: #c9b48a;
    --photo-steel: #9a9c9c;
  }
  html, body { margin: 0; padding: 0; overflow: hidden; background: var(--white); }
  .flyer {
    position: relative; width: 849px; height: 1200px; overflow: hidden;
    background: var(--white);
    font-family: "Noto Sans", "DejaVu Sans", sans-serif;
  }
  .backdrop { position: absolute; inset: 0; }
  .headline {
    position: absolute; left: 536px; top: 188px;
    transform: translate(-50%, -50%) rotate(-24.5deg);
    font-family: "Montserrat", sans-serif; font-weight: 800;
    font-size: 90px; letter-spacing: 1px; color: var(--green);
    white-space: nowrap; line-height: 1;
  }
  .tagline {
    position: absolute; left: 600px; top: 232px; width: 720px; height: 40px;
    transform: translate(-50%, -50%) rotate(-24.5deg);
    background: var(--green); color: var(--white);
    font-family: "Montserrat", sans-serif; font-weight: 700; font-size: 21px;
    letter-spacing: 1px; line-height: 40px; text-align: left;
    padding-left: 40px; box-sizing: border-box; white-space: nowrap;
  }
  .services-title {
    position: absolute; left: 243px; width: 606px; top: 460px;
    text-align: center; color: var(--white);
    font-size: 31px; font-weight: 400; letter-spacing: 0.5px;
  }
  .services-rule {
    position: absolute; left: 243px; width: 606px; top: 508px;
    height: 3px; background: var(--white);
  }
  .offer-list {
    position: absolute; left: 256px; top: 520px; width: 580px;
    margin: 0; padding: 0; list-style: none; color: var(--white);
    font-size: 25px; line-height: 35px;
  }
  .offer-list li { position: relative; padding-left: 50px; margin-bottom: 12px; white-space: nowrap; }
  .offer-list li::before {
    content: ""; position: absolute; left: 4px; top: 9px;
    width: 16px; height: 16px; border: 3px solid var(--white); border-radius: 50%;
  }
  .contact-rule {
    position: absolute; left: 585px; top: 924px; width: 2px; height: 222px;
    background: var(--photo-steel);
  }
  .contact-row {
    position: absolute; right: 252px; display: flex; align-items: center;
    gap: 8px; color: var(--green); font-size: 16px; white-space: nowrap;
    line-height: 22px;
  }
  .contact-key {
    width: 22px; height: 22px; border-radius: 50%; background: var(--white);
    color: var(--green); font-weight: 700; font-size: 13px;
    display: flex; align-items: center; justify-content: center;
  }
  .brand {
    position: absolute; left: 606px; top: 955px; width: 236px;
    display: flex; flex-direction: column; align-items: center; gap: 22px;
  }
  .brand-mark {
    width: 120px; height: 120px; border-radius: 50%; background: var(--green);
  }
  .brand-name {
    font-family: "Montserrat", sans-serif; font-weight: 700; font-size: 24px;
    letter-spacing: 2px; color: var(--green); text-align: center;
    line-height: 1; white-space: nowrap;
  }
</style>
</head>
<body>
<div class="flyer">
  <svg class="backdrop" width="849" height="1200" viewBox="0 0 849 1200">
    <polygon points="0,0 640,0 0,330" fill="var(--photo-blue)" role="img" aria-label="Photo: blue container interior stacked with lumber"/>
    <polygon points="243,440 849,171 849,822 243,822" fill="var(--panel-grey)"/>
    <polygon points="568,250 842,232 842,432 568,418" fill="var(--photo-steel)" role="img" aria-label="Photo: grey 20 foot shipping container"/>
    <polygon points="0,340 213,290 213,485 0,510" fill="var(--photo-light)" role="img" aria-label="Photo: white insulated container office interior"/>
    <polygon points="0,528 213,482 213,676 0,712" fill="var(--photo-blue)" role="img" aria-label="Photo: open-side container used as lumber storage"/>
    <polygon points="0,730 213,690 213,840 0,878" fill="var(--photo-sand)" role="img" aria-label="Photo: tan container with roll-up door"/>
    <polygon points="0,862 849,915 849,1160 0,1160" fill="var(--band-grey)"/>
    <polygon points="0,942 340,925 340,1150 0,1150" fill="var(--green-dark)" role="img" aria-label="Photo: green 40 foot shipping container"/>
  </svg>

  <div class="headline">CONTAINERS</div>
  <div class="tagline">Reasonable Customised Storage on the Go.</div>

  <div class="services-title">SALE, RENTAL &amp; CUSTOMIZATION</div>
  <div class="services-rule"></div>
  <ul class="offer-list">
    <li>20' and 40' shipping containers.</li>
    <li>New and Used Containers.</li>
    <li>Custom modify containers into storage<br>units, mobile offices, mobile job site<br>storage, command centers, pump<br>houses, garages, living space, the only<br>limit is the customers imagination.</li>
  </ul>

  <div class="contact-rule"></div>
  <div class="contact-row" style="top:962px;">Canada<span class="contact-key">A</span></div>
  <div class="contact-row" style="top:1007px;">800-tarnhld<span class="contact-key">P</span></div>
  <div class="contact-row" style="top:1053px;">info@tarnholdings.com<span class="contact-key">E</span></div>
  <div class="contact-row" style="top:1098px;">www.tarnholdings.com<span class="contact-key">W</span></div>

  <div class="brand">
    <div class="brand-mark"></div>
    <div class="brand-name">TARN HOLDINGS</div>
  </div>
</div>
</body>
</html>
```